Web Design Project

We are an IT System Integrator. We provide Norvik 500 ERP System, CRM etc. We also provide hardware, networking servicing. Please look at www.brinquot.com.sg. They provide the same service as us. We like to redesign our web site. I will attached the color that I prefer for reference.

Our website is www.ravdu.com.sg.  It has been created about 14 years ago.  We are trying to revamp it with a new look and information.   The new website must be informative, fast.    I have attached an attachment which show the color that I prefer(brownish golden).   

Our competitor (www.brinquot.com) is carrying the same trade as us.  They have all the informations In their website that we will like to have.  Therefore I recommend you to take a look at my competitor website and have a better   
understanding on the kind of information I would like to have for my new website.

This project is guarantee to the person with the best design.  We can have it guarantee.

Target Market(s)

Corporate and companies

Industry/Entity Type

Hardware

```html
<!DOCTYPE html>
<html lang="en">
<head>
<meta charset="utf-8">
<title>Ravdu Information System PTE LTD</title>
<link rel="stylesheet" href="https://fonts.googleapis.com/css2?family=Exo+2:wght@300;400;500&family=Arimo:wght@400;700&display=swap">
<style>
:root{
  --dark:#333333;
  --darker:#2a2a2a;
  --gold:#e0a82e;
  --gold-soft:#d8b25a;
  --text:#4a4a4a;
  --muted:#a4a4a4;
  --panel:#f2f2f2;
  --line:#dddddd;
  --white:#ffffff;
  --red:#a3281c;
}
*{box-sizing:border-box;margin:0;padding:0}
h1,h2,h3{font-weight:400}
html,body{width:1050px;height:1200px;overflow:hidden;background:var(--white)}
body{position:relative;font-family:"Arimo",Arial,sans-serif;color:var(--text)}
.site-header{position:absolute;left:0;top:0;width:1050px;height:136px;background:var(--dark)}
.brand{position:absolute;display:flex;align-items:center;gap:10px}
.brand-mark{width:22px;height:22px;border-radius:50%;background:var(--gold)}
.brand-name{font-family:"Exo 2",sans-serif;font-weight:400;color:var(--white);line-height:1.05}
.brand--header{left:160px;top:60px}
.brand--header .brand-name{font-size:23px}
.top-links{position:absolute;right:150px;top:16px;font-size:10px;color:var(--white)}
.top-links span{margin:0 4px}
.main-nav{position:absolute;left:390px;top:0;display:flex;height:78px}
.main-nav a{font-family:"Exo 2",sans-serif;font-size:15px;color:var(--white);text-decoration:none;padding:54px 8px 0;height:78px;white-space:nowrap}
.main-nav a.is-active{background:var(--darker);border-top:5px solid var(--gold);padding-top:49px;width:52px;text-align:center;padding-left:0;padding-right:0;margin-right:6px}
.header-social{position:absolute;left:822px;top:98px;display:flex;gap:10px}
.header-social i{display:block;width:20px;height:20px;border-radius:50%;background:var(--gold)}
.hero{position:absolute;left:0;top:136px;width:1050px;height:430px}
.hero-photo{position:absolute;inset:0;background:linear-gradient(100deg,#c9c6c0 0%,#e9e6e0 30%,#d8d4cd 55%,#a9a39a 80%,#cfcac2 100%)}
.hero-caption{position:absolute;left:436px;top:62px;width:467px;height:128px;background:rgba(255,255,255,.78);text-align:right;padding:8px 18px 0 0}
.hero-title{font-family:"Exo 2",sans-serif;font-weight:400;font-size:38px;color:#3a3a3a;letter-spacing:-.5px;white-space:nowrap}
.hero-sub{font-family:"Exo 2",sans-serif;font-weight:300;font-size:24px;color:#8a8a8a;line-height:1.2}
.slider-dots{position:absolute;left:468px;top:288px;display:flex;gap:14px}
.slider-dots i{width:12px;height:12px;border-radius:50%;background:var(--gold-soft);opacity:.7}
.slider-dots i:first-child{background:var(--gold);opacity:1}
.slider-arrow{position:absolute;top:334px;width:46px;height:46px;border-radius:50%;background:var(--white);box-shadow:0 1px 3px rgba(0,0,0,.3)}
.hero-curve{position:absolute;left:0;top:360px}
.service{position:absolute;top:454px;width:122px;height:140px}
.service svg{position:absolute;inset:0}
.service-label{position:absolute;left:0;width:122px;text-align:center;font-family:"Exo 2",sans-serif;font-size:14px;color:var(--gold);line-height:1.2}
.intro{position:absolute;left:150px;top:610px;width:750px;text-align:center}
.intro-title{font-family:"Exo 2",sans-serif;font-weight:400;font-size:34px;color:#2e2e2e;white-space:nowrap}
.intro-title em{font-style:normal;color:var(--gold)}
.intro-text{margin-top:10px;font-size:11.5px;line-height:15px;color:var(--muted);text-align:left}
.panel-bg{position:absolute;left:654px;top:754px;width:246px;height:248px;background:linear-gradient(90deg,#e9e9e9,#f7f7f7 20%,var(--panel))}
.article-title{position:absolute;left:157px;top:768px;font-family:"Exo 2",sans-serif;font-weight:300;font-size:19px;color:#333;line-height:1.02;white-space:nowrap}
.article-title span{display:block}
.byline{position:absolute;left:338px;top:770px;font-size:8.5px;color:#333;white-space:nowrap}
.byline b{color:var(--red)}
.article-card{position:absolute;left:157px;top:821px;width:260px;height:236px;border:1px solid var(--line)}
.article-photo{position:absolute;left:0;top:0;width:258px;height:115px;border:3px solid #aaa;background:radial-gradient(ellipse at 45% 40%,#c9a94e 0%,#4a7bb4 25%,#2b2b2b 60%,#111 100%)}
.article-text{position:absolute;left:10px;top:124px;width:238px;font-size:9.5px;line-height:15px;color:#333}
.share-row{position:absolute;left:15px;top:210px;display:flex;gap:12px;font-size:8.5px}
.share-row span{display:inline-flex}
.share-row b{background:#e7e7e7;border:1px solid #ccc;padding:1px 6px;font-weight:700;color:#445}
.share-row em{font-style:normal;border:1px solid #ccc;padding:1px 3px;margin-left:3px;color:#555}
.section-title{position:absolute;font-family:"Exo 2",sans-serif;font-weight:400;font-size:20px;color:#333;letter-spacing:.5px;white-space:nowrap}
.event{position:absolute;left:446px;width:168px;display:flex;gap:8px}
.event-date{flex:0 0 30px;height:32px;background:#3c3c3c;color:var(--white);text-align:center;font-family:"Exo 2",sans-serif;font-weight:500;line-height:1}
.event-date b{display:block;font-size:16px;padding-top:2px}
.event-date small{font-size:8px}
.event-text{font-size:9.5px;line-height:12px;color:#333}
.rule{position:absolute;height:1px;background:var(--line)}
.quote{position:absolute;left:672px;width:222px}
.quote-mark{position:absolute;font-family:Georgia,serif;font-size:28px;color:#555;line-height:1}
.quote-text{padding-left:22px;padding-right:22px;font-size:9px;line-height:13px;color:#333}
.quote-name{text-align:right;padding-right:42px;font-size:9px;font-style:italic;color:#333;margin-top:6px;line-height:12px}
.quote-name b{display:block}
.partners{position:absolute;left:434px;top:1006px;width:466px;height:56px;border:1px solid var(--line);background:linear-gradient(#fff,#efefef);display:flex;align-items:center}
.partner{flex:1;height:40px;display:flex;align-items:center;justify-content:center;border-right:1px solid var(--line);font-family:"Exo 2",sans-serif;color:#1e5e3a;white-space:nowrap}
.partner:last-child{border-right:none}
.site-footer{position:absolute;left:0;top:1094px;width:1050px;height:106px;background:var(--dark)}
.footer-nav{position:absolute;left:157px;top:36px;font-size:10.5px;color:var(--white)}
.footer-nav span{color:var(--gold);margin:0 5px}
.copyright{position:absolute;left:158px;top:63px;font-size:9.5px;color:#cfcfcf}
.footer-social{position:absolute;left:611px;top:51px;display:flex;gap:11px}
.footer-social i{display:block;width:27px;height:27px;border-radius:50%;background:var(--white)}
.brand--footer{left:774px;top:33px}
.brand--footer .brand-name{font-size:17px}
</style>
</head>
<body>

<header class="site-header">
  <div class="brand brand--header">
    <span class="brand-mark"></span>
    <span class="brand-name">Ravdu Information<br>System PTE LTD</span>
  </div>
  <div class="top-links">FAQs<span>|</span>Resources<span>|</span>Contact Us</div>
  <nav class="main-nav">
    <a class="is-active" href="#">HOME</a>
    <a href="#">ABOUT US</a>
    <a href="#">SOLUTIONS</a>
    <a href="#">SERVICES</a>
    <a href="#">EVENT &amp; PROMOTION</a>
    <a href="#">Our Clients</a>
  </nav>
  <div class="header-social"><i></i><i></i><i></i></div>
</header>

<section class="hero">
  <div class="hero-photo" role="img" aria-label="Smiling businesswoman in front of colleagues in a bright office"></div>
  <div class="hero-caption">
    <h1 class="hero-title">CUSTOMER RELATIONSHIP</h1>
    <p class="hero-sub">Shorten sales cycle and achieve total<br>customer satisfaction.</p>
  </div>
  <div class="slider-dots"><i></i><i></i><i></i><i></i><i></i><i></i></div>
  <div class="slider-arrow" style="left:37px">
    <svg width="46" height="46" viewBox="0 0 46 46"><path d="M27 13 L17 23 L27 33" fill="none" stroke="#111" stroke-width="5"/></svg>
  </div>
  <div class="slider-arrow" style="left:982px">
    <svg width="46" height="46" viewBox="0 0 46 46"><path d="M19 13 L29 23 L19 33" fill="none" stroke="#111" stroke-width="5"/></svg>
  </div>
  <svg class="hero-curve" width="1050" height="70" viewBox="0 0 1050 70"><path d="M0 60 Q525 -20 1050 60 L1050 70 L0 70 Z" fill="#fff"/></svg>
</section>

<div class="service" style="left:228px">
  <svg viewBox="0 0 122 140"><polygon points="61,0 122,35 122,105 61,140 0,105 0,35" fill="#2d2d2d"/>
    <rect x="38" y="32" width="10" height="38" fill="#e0a82e"/><rect x="52" y="32" width="34" height="26" rx="2" fill="none" stroke="#e0a82e" stroke-width="5"/><rect x="62" y="60" width="14" height="4" fill="#e0a82e"/><rect x="56" y="66" width="26" height="4" fill="#e0a82e"/></svg>
  <div class="service-label" style="top:88px">WORKSTATIONS</div>
</div>
<div class="service" style="left:391px">
  <svg viewBox="0 0 122 140"><polygon points="61,0 122,35 122,105 61,140 0,105 0,35" fill="#2d2d2d"/>
    <rect x="44" y="24" width="34" height="48" rx="3" fill="#e0a82e"/><g stroke="#2d2d2d" stroke-width="2"><line x1="48" y1="32" x2="74" y2="32"/><line x1="48" y1="38" x2="74" y2="38"/><line x1="48" y1="44" x2="74" y2="44"/><line x1="48" y1="50" x2="74" y2="50"/></g></svg>
  <div class="service-label" style="top:88px">SERVERS</div>
</div>
<div class="service" style="left:555px">
  <svg viewBox="0 0 122 140"><polygon points="61,0 122,35 122,105 61,140 0,105 0,35" fill="#2d2d2d"/>
    <rect x="46" y="26" width="30" height="12" fill="#e0a82e"/><rect x="36" y="40" width="50" height="22" rx="5" fill="#e0a82e"/><rect x="46" y="56" width="30" height="16" fill="#e0a82e" stroke="#2d2d2d" stroke-width="2"/></svg>
  <div class="service-label" style="top:88px">PRINTERS</div>
</div>
<div class="service" style="left:718px">
  <svg viewBox="0 0 122 140"><polygon points="61,0 122,35 122,105 61,140 0,105 0,35" fill="#2d2d2d"/>
    <rect x="54" y="18" width="14" height="8" fill="#e0a82e"/><circle cx="61" cy="48" r="20" fill="none" stroke="#e0a82e" stroke-width="6"/><circle cx="61" cy="48" r="7" fill="#e0a82e"/></svg>
  <div class="service-label" style="top:82px">SURVEILLANCE<br>CAMERA</div>
</div>

<section class="intro">
  <h2 class="intro-title">RAVDU INFORMATION SYSTEMS <em>PTE LTD (RIS)</em></h2>
  <p class="intro-text">is professionally managed by a core group of visionaries and technologists with decades of industry experience between them and backed by a team of trained professionals at all levels of operations. Perfection is a way of life at RIS. The organization has grown from a small beginning in 1993, to become a company of international repute for reliability. RIS has transformed from a Norvik Reseller to a company providing total IT solutions to companies in Singapore and the Asia region. RIS provides hardware maintenance, networking, software and consulting services.</p>
</section>

<div class="panel-bg"></div>

<h3 class="article-title"><span>HALVORSEN BANK'S</span><span>CAREFULLY ENGINEERED FUND</span></h3>
<div class="byline">By <b>TOM ARLOWE</b></div>
<article class="article-card">
  <div class="article-photo" role="img" aria-label="A bright multicoloured umbrella among dark umbrellas"></div>
  <p class="article-text">You would expect one of the biggest names in global finance to have a sophisticated pension fund, and on that measure the €7-billion ($9.2-billion) contractual trust arrangement (CTA) for Halvorsen Bank's German</p>
  <div class="share-row">
    <span><b>Share</b><em>191</em></span>
    <span><b>Like</b><em>2.6k</em></span>
    <span><b>Post</b><em>13</em></span>
  </div>
</article>

<h3 class="section-title" style="left:444px;top:768px">EVENTS &amp; NEWS</h3>
<div class="event" style="top:810px">
  <div class="event-date"><b>17</b><small>JAN</small></div>
  <p class="event-text">Lorem ipsum dolor sit amet, consectetuer adipiscing elit, sed diam nonummy nibh euismod tincidunt ut laoreet dolore.</p>
</div>
<div class="rule" style="left:446px;top:872px;width:166px"></div>
<div class="event" style="top:888px">
  <div class="event-date"><b>15</b><small>JAN</small></div>
  <p class="event-text">Lorem ipsum dolor sit amet, consectetuer adipiscing elit, sed diam nonummy nibh euismod tincidunt ut laoreet dolore magna aliquam erat volutpat.</p>
</div>
<div class="rule" style="left:446px;top:954px;width:166px"></div>

<h3 class="section-title" style="left:672px;top:768px">TESTIMONIALS</h3>
<div class="quote" style="top:806px">
  <span class="quote-mark" style="left:0;top:-4px">&ldquo;</span>
  <span class="quote-mark" style="right:0;top:12px">&rdquo;</span>
  <p class="quote-text">We would like to express our appreciation for the prompt and efficient service provided by</p>
  <p class="quote-name"><b>Owen Marsh</b>Chief Professor</p>
</div>
<div class="rule" style="left:694px;top:882px;width:196px"></div>
<div class="quote" style="top:892px">
  <span class="quote-mark" style="left:0;top:-4px">&ldquo;</span>
  <span class="quote-mark" style="right:0;top:12px">&rdquo;</span>
  <p class="quote-text">We would like to express our appreciation for the prompt and efficient service provided by</p>
  <p class="quote-name"><b>Owen Marsh</b>Chief Professor</p>
</div>

<h3 class="section-title" style="left:443px;top:966px">MEDIA PARTNERS</h3>
<div class="partners">
  <div class="partner"><svg width="40" height="40" viewBox="0 0 40 40"><circle cx="20" cy="20" r="18" fill="none" stroke="#2a3f8f" stroke-width="2"/></svg></div>
  <div class="partner" style="font-size:26px;font-weight:500">Tessel</div>
  <div class="partner" style="font-size:14px">Norvik Ledger ERP</div>
  <div class="partner"><svg width="80" height="24" viewBox="0 0 80 24"><rect x="0" y="2" width="80" height="20" fill="#4f7fc4"/></svg></div>
</div>

<footer class="site-footer">
  <div class="footer-nav">Home<span>/</span>About Us<span>/</span>Solutions<span>/</span>Services<span>/</span>Event &amp; Promotion<span>/</span>Our Clients</div>
  <p class="copyright">Copyrights © 2013 Ravdu Information System PTE LTD. All rights reserved.</p>
  <div class="footer-social"><i></i><i></i><i></i><i></i></div>
  <div class="brand brand--footer">
    <span class="brand-mark"></span>
    <span class="brand-name">Ravdu Information<br>System PTE LTD</span>
  </div>
</footer>

</body>
</html>
```